New Zealand Export company needs business cards

We need new business cards to match our new logo for a company based in New Zealand who deal specifically with the Pacific Islands. We source, consolidate and ship products out of New Zealand to the Pacific Islands. Will attach our old ones and also new logo.
Would like the Islands we deal with and the areas of work we have access to, to be included on the business cards.

Contact Information for Business Card

T +64 9 571 3048
F +64 9 571 6285
12-18 Kowhai Lane, Drury, 2113
PO Box 814, Drury, Auckland 2247, New Zealand
www.falconfreight.example.nz
E sales@falconfreight.example.nz

Font styles to use
Sans Serif

Colors
85abd2
33a6d7
ffffff

Requirements
Must have
• A company of PWM

```html
<!DOCTYPE html>
<html lang="en">
<head>
<meta charset="utf-8">
<title>Falcon Freight business card</title>
<link href="https://fonts.googleapis.com/css2?family=Work+Sans:wght@300;400;500;600&display=swap" rel="stylesheet">
<style>
  :root {
    --backdrop: #161616;
    --card: #1e1e1e;
    --card-edge: #2a2a2a;
    --silver: #c4c4c4;
    --silver-soft: #9a9a9a;
    --silver-dim: #808080;
    --blue-soft: #85abd2;
    --blue-bright: #33a6d7;
    --white: #ffffff;
  }
  * { margin: 0; padding: 0; box-sizing: border-box; }
  html, body {
    width: 1200px; height: 900px; overflow: hidden;
    background: var(--backdrop);
    font-family: "Work Sans", sans-serif;
  }
  .canvas {
    position: relative; width: 1200px; height: 900px;
    display: flex; flex-direction: column; align-items: center; justify-content: center; gap: 48px;
  }
  .card {
    position: relative;
    width: 640px; height: 366px;
    background: var(--card);
    border: 1px solid var(--card-edge);
  }
  .card--front {
    display: flex; flex-direction: column; align-items: center; justify-content: center; gap: 26px;
  }
  .brand { display: flex; align-items: center; gap: 18px; }
  .brand-mark { width: 22px; height: 22px; background: var(--blue-bright); }
  .brand-name {
    color: var(--silver);
    font-weight: 600; font-size: 40px; letter-spacing: 4px; text-transform: uppercase;
    white-space: nowrap;
  }
  .islands {
    color: var(--blue-soft);
    font-size: 13px; letter-spacing: 2px; text-transform: uppercase; white-space: nowrap;
  }
  .card--back {
    padding: 62px 40px 0 40px;
    display: flex; flex-direction: column; align-items: center;
  }
  .back-top { display: flex; align-items: center; gap: 30px; }
  .person { text-align: right; }
  .person-name {
    color: var(--silver); font-weight: 400; font-size: 26px; letter-spacing: 1px; text-transform: uppercase;
    line-height: 1.15; white-space: nowrap;
  }
  .person-role { color: var(--silver-soft); font-size: 14px; margin-top: 4px; white-space: nowrap; }
  .divider { width: 1px; height: 92px; background: var(--silver-soft); }
  .contact-list { list-style: none; display: flex; flex-direction: column; gap: 5px; }
  .contact-item {
    display: flex; align-items: center; gap: 10px;
    color: var(--silver); font-size: 14px; letter-spacing: 0.3px; white-space: nowrap;
  }
  .contact-icon { width: 13px; height: 13px; flex: none; }
  .services {
    margin-top: 34px;
    color: var(--blue-bright);
    font-size: 12px; font-weight: 500; letter-spacing: 2px; text-transform: uppercase; white-space: nowrap;
  }
  .address {
    margin-top: 26px; text-align: center;
    color: var(--silver-dim); font-size: 15px; line-height: 1.5; letter-spacing: 0.3px; white-space: nowrap;
  }
</style>
</head>
<body>
<main class="canvas">
  <section class="card card--front">
    <div class="brand">
      <span class="brand-mark"></span>
      <span class="brand-name">Falcon Freight</span>
    </div>
    <p class="islands">Fiji · Samoa · Tonga · Cook Islands · Vanuatu · Niue</p>
  </section>

  <section class="card card--back">
    <div class="back-top">
      <div class="person">
        <p class="person-name">Daniel Harper</p>
        <p class="person-role">Managing Partner</p>
      </div>
      <span class="divider"></span>
      <ul class="contact-list">
        <li class="contact-item">
          <svg class="contact-icon" viewBox="0 0 16 16" fill="none" stroke="#85abd2" stroke-width="1.6"><path d="M4 1.5l2.5 3-1.5 1.5c.8 2 2.5 3.7 4.5 4.5l1.5-1.5 3 2.5-1.5 2.5C7 14 2 9 1.5 3z"/></svg>
          +64 9 571 3048
        </li>
        <li class="contact-item">
          <svg class="contact-icon" viewBox="0 0 16 16" fill="none" stroke="#85abd2" stroke-width="1.6"><rect x="4" y="1.5" width="8" height="4"/><rect x="1.5" y="5.5" width="13" height="6"/><rect x="4" y="9.5" width="8" height="5"/></svg>
          +64 9 571 6285
        </li>
        <li class="contact-item">
          <svg class="contact-icon" viewBox="0 0 16 16" fill="none" stroke="#85abd2" stroke-width="1.6"><rect x="1.5" y="3.5" width="13" height="9"/><path d="M1.5 3.5L8 9l6.5-5.5"/></svg>
          sales@falconfreight.example.nz
        </li>
        <li class="contact-item">
          <svg class="contact-icon" viewBox="0 0 16 16" fill="none" stroke="#85abd2" stroke-width="1.4"><circle cx="8" cy="8" r="6.5"/><ellipse cx="8" cy="8" rx="3" ry="6.5"/><path d="M1.5 8h13"/></svg>
          www.falconfreight.example.nz
        </li>
      </ul>
    </div>
    <p class="services">Sourcing · Consolidation · Sea &amp; Air Freight · Customs</p>
    <p class="address">
      12-18 Kowhai Lane, Drury, 2113<br>
      PO Box 814, Drury, Auckland 2247, New Zealand
    </p>
  </section>
</main>
</body>
</html>
```